Tidal Oak Nutrition Webpage

Looking for a webpage for our new website, tidal oak nutrition.
We are going to be selling nutrition supplements. Our model site is www.morvelpeak.example as we want a feature product on the home page with a yellow order now button. However this website will have more than one product so we need another shop page.
Key Features:
- Home page with feature product and key selling points below it
- Each page has an order now button for our feature product
- Product page with categories (major) and products (sub-catagories) on a left hand navigation menu
- Top bar featuring "Shop", "About Us", "Contact" left justified and "My Account", "Checkout" right justified
- About Us Page with pictures on left and text describing:
- (first section) Left justified picture of red line as a flat red line on a monitor... ability to add text beside this
- (next section) Right justified picture of a blue line, but having the person in our logo climbing a hill with the blue line zig zagging up as the slope. Again we need the ability to add text to the left.
Our brand is modern and artistic with a focus on health and quality living. Think recycled blue construction paper for inspiration of what we're looking for.
Uploaded AI logos for different ideas...
Thanks!

```html
<!DOCTYPE html>
<html lang="en">
<head>
<meta charset="utf-8">
<title>Tidal Oak Nutrition</title>
<link href="https://fonts.googleapis.com/css2?family=Open+Sans:ital,wght@0,400;0,600;1,400&display=swap" rel="stylesheet">
<style>
:root{
  --brand:#0a86c9;
  --brand-dark:#0b5f8f;
  --ink:#444;
  --heading:#0d3550;
  --yellow:#fbeb8c;
  --line:#d8d8d8;
  --footer:#3f3f3f;
  --white:#fff;
}
*{box-sizing:border-box;margin:0;padding:0}
html,body{width:1200px;height:1200px;overflow:hidden;background:var(--white);font-family:"Open Sans",Arial,sans-serif;color:var(--ink)}
.page{position:relative;width:1200px;height:1200px}
.utility-bar{position:absolute;top:0;left:0;width:1200px;height:22px;border-bottom:1px solid #e4e4e4;font-size:10px;color:#555}
.utility-bar ul{position:absolute;right:154px;top:5px;list-style:none;display:flex;gap:16px}
.utility-bar li{display:flex;align-items:center;gap:4px}
.site-header{position:absolute;top:22px;left:0;width:1200px;height:87px}
.logo{position:absolute;left:151px;top:12px;display:flex;align-items:center;gap:6px}
.logo-mark{width:62px;height:62px;border-radius:50%;background:var(--brand)}
.logo-name{font-size:18px;font-weight:600;color:var(--brand);line-height:17px;width:90px}
.main-nav{position:absolute;right:154px;top:21px;display:flex;height:46px}
.main-nav a{display:flex;align-items:center;padding:0 16px;font-size:15px;color:var(--brand);text-decoration:none;border-left:1px solid var(--line)}
.main-nav a:first-child{border-left:none}
.main-nav a:last-child{padding-right:2px}
.hero{position:absolute;top:109px;left:0;width:1200px;height:323px;background:linear-gradient(180deg,#b8cdd8 0%,#7fa3bd 35%,#9ab7c6 62%,#c9c0b2 100%)}
.hero-photo{position:absolute;inset:0}
.hero-products{position:absolute;left:769px;top:154px;width:269px;height:163px;background:linear-gradient(180deg,#2b2f8c,#3d4bb0 55%,#9aa3c4);border-radius:10px 10px 4px 4px}
.hero-title{position:absolute;left:559px;top:30px;width:460px;font-size:28px;line-height:35px;color:var(--heading);font-weight:400}
.hero-cta{position:absolute;left:560px;top:118px;width:160px;height:63px;background:#7b7b7b;padding:10px 7px 8px}
.btn-order{display:flex;align-items:center;justify-content:center;background:var(--yellow);color:var(--brand-dark);font-style:italic;text-decoration:none}
.hero-cta .btn-order{width:100%;height:100%;font-size:20px}
.slider-dots{position:absolute;left:566px;top:290px;display:flex;gap:7px}
.slider-dots span{width:8px;height:8px;border-radius:50%;background:#111}
.slider-dots span.active{background:#e02020}
.sidebar{position:absolute;left:152px;top:453px;width:243px}
.categories{width:240px}
.categories h2{height:30px;background:var(--brand);color:var(--white);font-size:14px;font-weight:600;padding:6px 11px;margin-bottom:4px}
.categories ul{list-style:none;background:var(--brand);padding:14px 10px 19px}
.categories li{height:32.3px;display:flex;align-items:center;gap:12px;padding-left:13px;font-size:12.5px;color:var(--white);border-bottom:1px solid rgba(0,50,90,.35)}
.categories li:last-child{border-bottom:none}
.newsletter{position:absolute;top:414px;left:-2px;width:245px}
.newsletter h2{font-size:18.5px;font-weight:400;color:var(--brand-dark)}
.newsletter p{margin-top:6px;font-size:11.3px;line-height:16.5px;color:#555;padding-left:2px}
.newsletter .email{position:absolute;top:94px;left:2px;width:243px;height:34px;border:1px solid #ccc;font-size:11.5px;color:#666;padding:9px 13px;font-family:inherit}
.newsletter .subscribe{position:absolute;top:139px;left:160px;width:86px;height:32px;background:var(--brand-dark);color:var(--white);font-size:13px;font-style:italic;font-weight:600;display:flex;align-items:center;justify-content:center}
.featured{position:absolute;left:426px;top:453px;width:622px}
.featured h2{font-size:19px;font-weight:400;color:var(--brand-dark);margin-top:3px}
.product-card{position:absolute;width:189px;height:288px;border:1px solid #ccc;background:var(--white);text-align:center;box-shadow:0 4px 4px -3px rgba(0,0,0,.25)}
.product-shot{display:block;margin:17px auto 0;width:86px;height:148px;border-radius:10px 10px 6px 6px;background:linear-gradient(180deg,#202678,#3c4cb4 60%,#8d98c6)}
.product-shot.dark{background:linear-gradient(180deg,#111,#3a3a3a 60%,#6d6d6d);border-radius:20px}
.product-shot.light{background:linear-gradient(180deg,#eceff2,#c9d1d8 60%,#7a8c99);border-radius:20px}
.product-shot.navy{background:linear-gradient(180deg,#0d1a5a,#1d2d86 60%,#3b4a9a);border-radius:6px}
.product-card h3{margin-top:20px;font-size:16.5px;font-weight:400;color:var(--brand);letter-spacing:.2px}
.product-card p{font-size:11.3px;line-height:15px;color:#555;margin-top:1px}
.product-card .btn-order{width:103px;height:29px;margin:9px auto 0;font-size:16.5px}
.view-all{position:absolute;left:482px;top:654px;width:138px;height:30px;background:var(--brand);color:var(--white);font-size:14px;font-weight:600;display:flex;align-items:center;justify-content:center}
.site-footer{position:absolute;left:0;top:1148px;width:1200px;height:52px;background:var(--footer);color:var(--white);font-size:11.5px}
.follow{position:absolute;left:151px;top:15px;display:flex;align-items:center;gap:8px}
.follow .social{width:22px;height:22px;background:#4a90d0;border-radius:3px;margin-left:4px}
.copyright{position:absolute;right:154px;top:19px}
</style>
</head>
<body>
<div class="page">

  <div class="utility-bar">
    <ul>
      <li><svg width="9" height="9" viewBox="0 0 9 9"><circle cx="4.5" cy="2.5" r="2.2" fill="#333"/><path d="M0.5 9 Q4.5 3.5 8.5 9Z" fill="#333"/></svg>My Account</li>
      <li><svg width="13" height="10" viewBox="0 0 13 10"><path d="M0.5 1H2.5L4 7H11L12 3H3" fill="none" stroke="#333" stroke-width="1.1"/><circle cx="5" cy="9" r="0.9" fill="#333"/><circle cx="10" cy="9" r="0.9" fill="#333"/></svg>Checkout</li>
    </ul>
  </div>

  <header class="site-header">
    <div class="logo">
      <div class="logo-mark"></div>
      <div class="logo-name">tidal oak nutrition</div>
    </div>
    <nav class="main-nav">
      <a href="#">Shop</a>
      <a href="#">About Us</a>
      <a href="#">Contact</a>
    </nav>
  </header>

  <section class="hero">
    <div class="hero-photo" role="img" aria-label="Smiling couple walking hand in hand along a beach with waves behind them"></div>
    <div class="hero-products" role="img" aria-label="Three supplement tubs in a row"></div>
    <h1 class="hero-title">We are going to be selling nutrition supplements</h1>
    <div class="hero-cta"><a class="btn-order" href="#">Order Now</a></div>
    <div class="slider-dots"><span></span><span></span><span class="active"></span><span></span><span></span></div>
  </section>

  <aside class="sidebar">
    <div class="categories">
      <h2>CATEGORIES</h2>
      <ul>
        <li><svg width="4" height="6"><path d="M0 0L4 3L0 6Z" fill="#fff"/></svg>Lorem ipsum dolor sit amet</li>
        <li><svg width="4" height="6"><path d="M0 0L4 3L0 6Z" fill="#fff"/></svg>Praesent nec erat tristique</li>
        <li><svg width="4" height="6"><path d="M0 0L4 3L0 6Z" fill="#fff"/></svg>Praesent egestas augue</li>
        <li><svg width="4" height="6"><path d="M0 0L4 3L0 6Z" fill="#fff"/></svg>Proin feugiat magna eu</li>
        <li><svg width="4" height="6"><path d="M0 0L4 3L0 6Z" fill="#fff"/></svg>\Nullam vehicula eros</li>
        <li><svg width="4" height="6"><path d="M0 0L4 3L0 6Z" fill="#fff"/></svg>Suspendisse bibendum</li>
        <li><svg width="4" height="6"><path d="M0 0L4 3L0 6Z" fill="#fff"/></svg>Curabitur ac dui volutpat</li>
        <li><svg width="4" height="6"><path d="M0 0L4 3L0 6Z" fill="#fff"/></svg>Suspendisse dignissim</li>
        <li><svg width="4" height="6"><path d="M0 0L4 3L0 6Z" fill="#fff"/></svg>Quisque molestie</li>
        <li><svg width="4" height="6"><path d="M0 0L4 3L0 6Z" fill="#fff"/></svg>Curabitur in arcu</li>
      </ul>
    </div>
    <div class="newsletter">
      <h2>NEWSLETTER SIGNUP</h2>
      <p>Contrary to popular belief, Lorem Ipsum is not simply random text. It has roots in a piece of classical</p>
      <div class="email">Enter your Email id</div>
      <div class="subscribe">SUBSCRIBE</div>
    </div>
  </aside>

  <main class="featured">
    <h2>Feature Products</h2>

    <article class="product-card" style="left:2px;top:42px">
      <span class="product-shot" role="img" aria-label="Blue supplement tub"></span>
      <h3>Praesent nec erat</h3>
      <p>Contrary to popular belief,<br>Lorem Ipsum is not simply</p>
      <a class="btn-order" href="#">Order Now</a>
    </article>
    <article class="product-card" style="left:216px;top:42px">
      <span class="product-shot" role="img" aria-label="Blue supplement tub"></span>
      <h3>Praesent nec erat</h3>
      <p>Contrary to popular belief,<br>Lorem Ipsum is not simply</p>
      <a class="btn-order" href="#">Order Now</a>
    </article>
    <article class="product-card" style="left:431px;top:42px">
      <span class="product-shot" role="img" aria-label="Blue supplement tub"></span>
      <h3>Praesent nec erat</h3>
      <p>Contrary to popular belief,<br>Lorem Ipsum is not simply</p>
      <a class="btn-order" href="#">Order Now</a>
    </article>

    <article class="product-card" style="left:2px;top:351px">
      <span class="product-shot dark" role="img" aria-label="Black protein powder tub"></span>
      <h3>Praesent nec erat</h3>
      <p>Contrary to popular belief,<br>Lorem Ipsum is not simply</p>
      <a class="btn-order" href="#">Order Now</a>
    </article>
    <article class="product-card" style="left:216px;top:351px">
      <span class="product-shot light" role="img" aria-label="White shake powder tub"></span>
      <h3>Praesent nec erat</h3>
      <p>Contrary to popular belief,<br>Lorem Ipsum is not simply</p>
      <a class="btn-order" href="#">Order Now</a>
    </article>
    <article class="product-card" style="left:431px;top:351px">
      <span class="product-shot navy" role="img" aria-label="Navy multivitamin bottle"></span>
      <h3>Praesent nec erat</h3>
      <p>Contrary to popular belief,<br>Lorem Ipsum is not simply</p>
      <a class="btn-order" href="#">Order Now</a>
    </article>

    <a class="view-all">View All Products</a>
  </main>

  <footer class="site-footer">
    <div class="follow">Follow us <span class="social"></span><span class="social"></span></div>
    <div class="copyright">Copyrights @ 2013 All Rights Reserved</div>
  </footer>

</div>
</body>
</html>
```